IT Company based on Biology Business Needs a PowerPoint Design

We need a powerpoint design for a new company called 'Vast KELP'. We develop the machine learning solutions especially focused on deep learning algorithms for biology industry. Our initial product is a vision detection on biological images to help doctors diagnose the symptoms. We would like to see designs that use the color green.

Industry/Entity Type

Biotechnology

Requirements
Nice to have
• Lots of slide templates with company logo's look and feel

```html
<!DOCTYPE html>
<html lang="en">
<head>
<meta charset="utf-8">
<title>Vast KELP – Slide Templates</title>
<link href="https://fonts.googleapis.com/css2?family=Carlito:wght@400;700&display=swap" rel="stylesheet">
<style>
  :root {
    --canvas: #ffffff;
    --leaf: #acd48c;
    --frame: #7cc04b;
    --brand: #5cb531;
    --forest: #1e7a2f;
    --ink: #1a1a1a;
    --muted: #707070;
    --footer-light: #9cc97a;
    --photo-a: #f2f7fb;
    --photo-b: #c9dcea;
    --photo-c: #2f6f96;
  }
  * { box-sizing: border-box; margin: 0; padding: 0; }
  html, body { width: 1200px; height: 1200px; overflow: hidden; background: var(--canvas); }
  body { position: relative; font-family: "Carlito", "Calibri", sans-serif; color: var(--ink); }

  .slide {
    position: absolute;
    width: 491px; height: 368px;
    background: var(--canvas);
    border-top: 3px solid var(--leaf);
    border-left: 6px solid var(--leaf);
    border-right: 2px solid var(--leaf);
    overflow: hidden;
  }
  .col-a { left: 107px; } .col-b { left: 610px; }
  .row-1 { top: 28px; } .row-2 { top: 409px; } .row-3 { top: 800px; }

  .slide--cover { background: var(--leaf); border: none; }

  .brand {
    position: absolute; left: 14px; top: 13px;
    display: flex; align-items: center; gap: 4px;
    font-size: 12px; color: var(--brand); letter-spacing: -0.3px;
  }
  .brand__dot { width: 8px; height: 8px; border-radius: 50%; background: var(--brand); }

  .slide-title {
    position: absolute; right: 30px; top: 22px;
    font-size: 16px; font-weight: 700; color: var(--forest);
  }

  .bullets { position: absolute; left: 22px; top: 64px; list-style: none; font-size: 12px; }
  .bullets li::before { content: "•"; margin-right: 14px; font-size: 10px; }

  .footer {
    position: absolute; left: 22px; bottom: 7px;
    font-size: 7px; font-weight: 700; color: var(--forest);
  }
  .footer__light { color: var(--footer-light); font-weight: 400; }
  .page-no {
    position: absolute; right: 30px; bottom: 7px;
    font-size: 7px; font-weight: 700; color: var(--forest);
  }

  .cover__mark {
    position: absolute; left: 24px; top: 44px;
    display: flex; align-items: center; gap: 12px;
    font-size: 56px; color: #ffffff; letter-spacing: -2px;
  }
  .cover__circle { width: 40px; height: 40px; border-radius: 50%; background: #ffffff; }
  .cover__title { position: absolute; left: 121px; top: 150px; font-size: 22px; font-weight: 700; color: var(--forest); }
  .cover__subtitle { position: absolute; left: 122px; top: 198px; font-size: 12px; color: #ffffff; }

  .divider__kicker { position: absolute; left: 37px; top: 139px; font-size: 12px; color: var(--muted); }
  .divider__header { position: absolute; left: 38px; top: 164px; font-size: 24px; font-weight: 700; color: var(--forest); }

  .image-frame {
    position: absolute;
    border: 9px solid var(--frame);
    background: var(--canvas);
    box-shadow: 2px 3px 4px rgba(0,0,0,0.25);
  }
  .image-frame--wide { left: 26px; top: 55px; width: 413px; height: 282px; }
  .image-frame--side { left: 248px; top: 59px; width: 205px; height: 246px; }
  .photo {
    width: 100%; height: 100%;
    background: radial-gradient(circle at 62% 45%, var(--photo-c) 0%, var(--photo-b) 35%, var(--photo-a) 75%);
  }
</style>
</head>
<body>

  <section class="slide slide--cover col-a row-1">
    <div class="cover__mark"><span class="cover__circle"></span>VAST KELP</div>
    <h1 class="cover__title">Title</h1>
    <p class="cover__subtitle">Subtitle</p>
  </section>

  <section class="slide col-b row-1">
    <div class="brand"><span class="brand__dot"></span>VAST KELP</div>
    <h2 class="slide-title">Header</h2>
    <ul class="bullets"><li>Bullet text</li></ul>
    <p class="footer"><span class="footer__light">Copyright © VastKelp</span> - Confidental</p>
    <span class="page-no">2</span>
  </section>

  <section class="slide col-a row-2">
    <div class="brand"><span class="brand__dot"></span>VAST KELP</div>
    <p class="divider__kicker">Section</p>
    <h2 class="divider__header">DIVIDER HEADER</h2>
    <p class="footer"><span class="footer__light">Copyright © VastKelp</span> - Confidental</p>
    <span class="page-no">3</span>
  </section>

  <section class="slide col-b row-2">
    <div class="brand"><span class="brand__dot"></span>VAST KELP</div>
    <h2 class="slide-title">Image Frame</h2>
    <div class="image-frame image-frame--wide"></div>
    <p class="footer">Copyright © VastKelp - Confidental</p>
    <span class="page-no">4</span>
  </section>

  <section class="slide col-a row-3">
    <div class="brand"><span class="brand__dot"></span>VAST KELP</div>
    <h2 class="slide-title">Image Frame - Example</h2>
    <div class="image-frame image-frame--wide">
      <div class="photo" role="img" aria-label="Gloved doctor with stethoscope touching a screen of blue hexagonal medical icons"></div>
    </div>
    <p class="footer">Copyright © VastKelp - Confidental</p>
    <span class="page-no">5</span>
  </section>

  <section class="slide col-b row-3">
    <div class="brand"><span class="brand__dot"></span>VAST KELP</div>
    <h2 class="slide-title">Content &amp; Frame</h2>
    <div class="image-frame image-frame--side">
      <div class="photo" role="img" aria-label="Cropped view of a gloved doctor with stethoscope and blue medical icons"></div>
    </div>
    <p class="footer">Copyright © VastKelp - Confidental</p>
    <span class="page-no">6</span>
  </section>

</body>
</html>
```